Flyer Design - Child Care Centre

I need a flyer design (d/sided), full colour for a Child Care Centre that I have recently bought. Check out my website (tiny-sprouts.com.au) for information on what we do, our services, philosophy, fees and hours of operation.

The purpose of this flyer is to advertise our services as a child care centre (under new management) to the local community and with various hospitals.

The flyer should embody our philosophy, the text on my home page (particularly our QX focus) and some of the parent testimonials. It should also include my logo and Zibb (refer attached AI and jpeg files, eps available on request).

Feel free to add stock photo's of kids and cartoon characters and use the following CMYK colours if incorporating any coloured text. Green: C-78, M-0, Y-100, K-0 Magenta: C-0, M-100, Y-33, K-10

```html
<!DOCTYPE html>
<html lang="en">
<head>
<meta charset="utf-8">
<title>Tiny Sprouts Child Care Flyer</title>
<link href="https://fonts.googleapis.com/css2?family=Comic+Neue:wght@400;700&display=swap" rel="stylesheet">
<style>
  :root {
    --backdrop: #8c8c8c;
    --paper: #f4f0e4;
    --magenta: #d0145a;
    --green: #2ea44a;
    --band: #d9a779;
    --band-edge: #e89a5c;
    --art-skin: #e9c6a0;
    --art-warm: #f0b08a;
  }
  * { box-sizing: border-box; margin: 0; padding: 0; }
  html, body { width: 1200px; height: 900px; overflow: hidden; }
  body {
    background: var(--backdrop);
    font-family: "Comic Neue", "Comic Sans MS", cursive;
    display: flex; align-items: center; justify-content: center;
  }
  .flyer {
    position: relative;
    width: 608px; height: 860px;
    background: var(--paper);
    overflow: hidden;
  }
  .intro {
    position: absolute; left: 44px; right: 40px; top: 44px;
    color: var(--magenta); font-weight: 700;
    font-size: 13.6px; line-height: 1.28; text-align: justify;
  }
  .intro p { margin-bottom: 0; }
  .social {
    position: absolute; left: 44px; top: 470px;
    color: var(--green); font-weight: 700; font-size: 12.5px; line-height: 1.25;
  }
  .social .handle { display: block; margin-bottom: 8px; }
  .band {
    position: absolute; left: 0; right: 0; top: 590px; height: 92px;
    background: var(--band);
    border-bottom: 8px solid var(--band-edge);
  }
  .art-girl {
    position: absolute; left: 150px; top: 480px; width: 260px; height: 215px;
    border-radius: 14px;
    background: radial-gradient(ellipse at 35% 45%, var(--art-warm), var(--art-skin) 55%, rgba(233,198,160,0) 78%);
  }
  .art-sun {
    position: absolute; left: 360px; top: 450px; width: 44px; height: 36px;
    border-radius: 50%;
    background: radial-gradient(circle, rgba(240,120,120,.55), rgba(240,120,120,0) 70%);
  }
  .hours {
    position: absolute; right: 40px; top: 612px; width: 170px;
    text-align: center; font-weight: 700; line-height: 1.15;
  }
  .hours .label { color: var(--green); font-size: 17px; letter-spacing: 1px; }
  .hours .days, .hours .times { color: var(--magenta); font-size: 17px; }
  .hours .note { color: var(--green); font-size: 12.5px; font-weight: 400; }
  .address {
    position: absolute; left: 44px; top: 708px;
    color: var(--green); font-weight: 700; font-size: 15px; line-height: 1.25;
  }
  .mascot {
    position: absolute; left: 262px; top: 748px;
    display: flex; align-items: center; gap: 8px;
    color: var(--green); font-weight: 700; font-size: 22px;
  }
  .mascot .dot { width: 14px; height: 14px; border-radius: 50%; background: var(--green); }
  .contact {
    position: absolute; right: 40px; top: 760px;
    color: var(--green); font-weight: 700; font-size: 15px; line-height: 1.35; text-align: right;
  }
  .stripe {
    position: absolute; left: 0; right: 0; top: 718px; height: 6px;
    background: var(--band-edge); opacity: .0;
  }
</style>
</head>
<body>
  <main class="flyer">
    <section class="intro">
      <p>The QX Convention on the Rights of the Child states that 'All children have the right to an education that lays a foundation for the rest of their lives, maximises their ability, and respects their family, cultural and other identities and languages'.</p>
      <p>Our educators, guided by the Early Years Learning Framework, will reinforce in their daily practice the principles as laid out in the QX Convention on the Rights of the Child.</p>
      <p>It is through the passion, dedication, and commitment of our educators and carers that a safe, caring and fun environment is provided for your children.</p>
      <p>We provide a child care environment that enhances the emotional and physical health of your child, stimulates the children's involvement in activities and encourages self-esteem and a sense of achievement.</p>
      <p>We encourage all families to visit our centre regularly so as to experience and engage in our positive and relaxing atmosphere and to meet and interact with our educators.</p>
      <p>Tiny Sprouts child care centre - Long Day Care, Before &amp; After School Care (Schoolies/OSHC) and Vacation Care for children.</p>
      <p>Tiny Sprouts is located in Wattle Grove, WA 6107. We look forward to welcoming you and your children at our centre.</p>
    </section>

    <div class="social">
      <span>Like Us</span>
      <span class="handle">@tinysproutsOZ</span>
      <span>Follow our tweets</span>
      <span class="handle">@TinySproutsAU</span>
    </div>

    <div class="band"></div>
    <div class="art-sun" role="img" aria-label="Hand-drawn crayon sun"></div>
    <div class="art-girl" role="img" aria-label="Cartoon girl with pigtails sitting and drawing a boat with crayons"></div>

    <div class="hours">
      <div class="label">OPEN</div>
      <div class="days">Monday - Friday</div>
      <div class="times">6:00am - 6:00pm</div>
      <div class="note">(except public holidays)</div>
    </div>

    <address class="address">
      118 Banksia Road,<br>
      Wattle Grove,<br>
      Western Australia 6107
    </address>

    <div class="mascot">
      <span class="dot"></span>
      <span>Zibb</span>
    </div>

    <div class="contact">
      Phone (08) 9400 1275<br>
      Email:<br>
      enquiries@tiny-sprouts.com.au
    </div>
  </main>
</body>
</html>
```